Security Warning Sign

We have an existing sign that needs an update. I have attached a picture of the current square sign. We need to maintain the same wording. It needs to be professional and appropriate to attach to our customers fence. Also attached is a copy of our building sign which may lend some inspiration and hopefully the ai format will assist. The final sign will be 600mm x 600mmOur website is www.halvorngate.com.au

```html
<!DOCTYPE html>
<html lang="en">
<head>
<meta charset="utf-8">
<title>Security Warning Sign – Halvorngate Security Services</title>
<link rel="stylesheet" href="https://fonts.googleapis.com/css2?family=Anton&family=Roboto+Condensed:wght@700;800&family=Open+Sans:wght@800&display=swap">
<style>
  :root {
    --orange: #f48420;
    --ink: #262626;
    --white: #ffffff;
    --camera-light: #e8e8e8;
    --camera-dark: #3a3a3a;
  }
  html, body {
    margin: 0;
    padding: 0;
    width: 1200px;
    height: 1200px;
    overflow: hidden;
    background: var(--white);
  }
  .sign {
    position: relative;
    width: 1200px;
    height: 1200px;
    background: var(--white);
  }
  .sign-art {
    position: absolute;
    inset: 0;
    width: 1200px;
    height: 1200px;
    display: block;
  }
  .headline {
    font-family: "Anton", "Impact", sans-serif;
    fill: var(--white);
  }
  .notice-line {
    font-family: "Roboto Condensed", "Arial Narrow", sans-serif;
    font-weight: 700;
    fill: var(--ink);
  }
  .company-name {
    font-family: "Open Sans", "Arial", sans-serif;
    font-weight: 800;
    fill: var(--ink);
  }
  .phone-number {
    font-family: "Open Sans", "Arial", sans-serif;
    font-weight: 800;
    fill: var(--orange);
  }
  .website {
    font-family: "Roboto Condensed", "Arial Narrow", sans-serif;
    font-weight: 800;
    fill: var(--ink);
  }
  .camera-photo {
    position: absolute;
    left: 829px;
    top: 222px;
    width: 296px;
    height: 234px;
    border-radius: 40% 40% 48% 48%;
    background: radial-gradient(circle at 50% 65%, var(--camera-dark) 0 30%, var(--camera-light) 31% 100%);
  }
</style>
</head>
<body>
<main class="sign">
  <svg class="sign-art" viewBox="0 0 1200 1200" xmlns="http://www.w3.org/2000/svg">
    <rect class="warning-panel" width="1200" height="996" fill="var(--orange)"/>

    <text class="headline" x="20" y="195" font-size="196" textLength="1162" lengthAdjust="spacingAndGlyphs">WARNING</text>

    <text class="notice-line" x="50" y="363" font-size="164" textLength="531" lengthAdjust="spacingAndGlyphs">ELECTRONIC</text>
    <text class="notice-line" x="50" y="554" font-size="164" textLength="627" lengthAdjust="spacingAndGlyphs">SURVEILLANCE</text>
    <text class="notice-line" x="46" y="745" font-size="164" textLength="1110" lengthAdjust="spacingAndGlyphs">AND RECORDING DEVICES</text>
    <text class="notice-line" x="50" y="936" font-size="164" textLength="1110" lengthAdjust="spacingAndGlyphs" xml:space="preserve">INSTALLED  IN  THE  AREA</text>

    <g class="company">
      <circle class="company-dot" cx="98" cy="1092" r="70" fill="var(--orange)"/>
      <text class="company-name" x="211" y="1075" font-size="42" textLength="280" lengthAdjust="spacingAndGlyphs">HALVORNGATE</text>
      <text class="company-name" x="211" y="1118" font-size="42" textLength="213" lengthAdjust="spacingAndGlyphs">SECURITY</text>
      <text class="company-name" x="211" y="1160" font-size="42" textLength="204" lengthAdjust="spacingAndGlyphs">SERVICES</text>
    </g>

    <g class="phone">
      <svg class="phone-icon" x="528" y="1022" width="74" height="74" viewBox="0 0 24 24" aria-hidden="true">
        <path fill="var(--orange)" d="M6.6 10.8a15.1 15.1 0 0 0 6.6 6.6l2.2-2.2a1 1 0 0 1 1-.25 11.4 11.4 0 0 0 3.6.57 1 1 0 0 1 1 1V20a1 1 0 0 1-1 1A17 17 0 0 1 3 4a1 1 0 0 1 1-1h3.5a1 1 0 0 1 1 1c0 1.25.2 2.45.57 3.57a1 1 0 0 1-.25 1z"/>
      </svg>
      <text class="phone-number" x="624" y="1090" font-size="87" textLength="553" lengthAdjust="spacingAndGlyphs">1300 555 017</text>
    </g>

    <text class="website" x="539" y="1166" font-size="51" textLength="644" lengthAdjust="spacingAndGlyphs">WWW.HALVORNGATE.COM.AU</text>
  </svg>

  <div class="camera-photo" role="img" aria-label="Photo of a white dome security camera"></div>
</main>
</body>
</html>
```